Tri fold brochure for construction company

Looking for a tri fold brochure which utilizes black, teal and white colors. Logo must be on main page (several files with Logo attached)
Inside brochure.
1st Page - 3D photo/sketch/drawing of a complete residential high rise building with windows, balconies and elements of concrete and bricks.
2nd Page - Text which will outline company's main activities. file with text is attached.
3rd Page - photo/sketch/drawing of underground parking garage which shows columns/beams/walls/ and garage entrance/exit ramp. Can be multiple photos.
Back of brochure
1st page - company logo
2nd page - please propose something.
3rd page - company message with address and contact info (to be provided)
Back ground color of brochure should complement our logo/photos/sketches/drawings.
Alternative design options are welcome.

```html
<!DOCTYPE html>
<html lang="en">
<head>
<meta charset="utf-8">
<title>Construction Services Tri-fold Brochure – Inside Spread</title>
<link href="https://fonts.googleapis.com/css2?family=Open+Sans:wght@400;600;700;800&display=swap" rel="stylesheet">
<style>
  :root {
    --backdrop: #3a3a3a;
    --teal: #1f9a82;
    --teal-deep: #17806c;
    --ink: #1b1b1b;
    --paper: #ffffff;
    --text-soft: #e6f4f0;
    --photo-sky: #6fa6d8;
    --photo-warm: #c9683a;
    --hat-light: #f6d640;
    --hat-dark: #e2b313;
  }
  * { box-sizing: border-box; margin: 0; padding: 0; }
  html, body { width: 1200px; height: 800px; overflow: hidden; }
  body {
    background: var(--backdrop);
    font-family: "Open Sans", sans-serif;
    display: flex; align-items: center; justify-content: center;
  }
  .brochure {
    width: 1110px; height: 760px;
    display: grid; grid-template-columns: repeat(3, 1fr);
    box-shadow: 0 20px 50px rgba(0,0,0,.45);
  }
  .panel { position: relative; overflow: hidden; }

  /* Panel 1 – photo */
  .panel--photo { background: var(--ink); }
  .photo-area {
    position: absolute; top: 34px; left: 0; right: 0; bottom: 0;
    background: linear-gradient(180deg, var(--photo-sky) 0%, #a9c7e2 22%, #b9a79a 45%, var(--photo-warm) 62%, #7a8c5a 82%, #a8a46a 100%);
  }

  /* Panels 2 & 3 – teal text */
  .panel--text {
    background: linear-gradient(180deg, var(--teal) 0%, var(--teal-deep) 100%);
    color: var(--paper);
    padding: 40px 34px 0 38px;
  }
  .section-title { font-size: 24px; font-weight: 800; line-height: 1.1; margin-top: 18px; }
  .section-title:first-child { margin-top: 0; }
  .title-rule { width: 34px; height: 5px; border-radius: 3px; background: var(--paper); margin: 8px 0 10px; }
  .group-title { font-size: 15px; font-weight: 700; margin-top: 10px; }
  .checklist { list-style: none; margin-top: 3px; }
  .checklist li {
    font-size: 12.5px; line-height: 1.38; color: var(--text-soft);
    padding-left: 17px; position: relative;
  }
  .checklist li::before {
    content: ""; position: absolute; left: 2px; top: 5px;
    width: 8px; height: 4px;
    border-left: 2px solid var(--paper); border-bottom: 2px solid var(--paper);
    transform: rotate(-45deg);
  }
  .checklist li.continued::before { display: none; }

  .panel--services-extra .section-title { margin-top: 26px; }
  .footer-art { position: absolute; left: 0; bottom: 0; width: 100%; height: 250px; }
  .hat-photo {
    position: absolute; right: 24px; bottom: 96px;
    width: 150px; height: 112px;
    background: linear-gradient(160deg, var(--hat-light) 0%, var(--hat-dark) 100%);
  }
</style>
</head>
<body>
  <main class="brochure">
    <section class="panel panel--photo">
      <div class="photo-area" role="img" aria-label="Photo of a modern residential apartment building with balconies, behind a courtyard playground"></div>
    </section>

    <section class="panel panel--text panel--services">
      <h2 class="section-title">Building Envelope:</h2>
      <div class="title-rule"></div>
      <h3 class="group-title">Concrete repairs</h3>
      <ul class="checklist">
        <li>Balcony slabs</li><li>Shear Walls</li><li>Beams &amp; Columns</li>
      </ul>
      <h3 class="group-title">Masonry repairs</h3>
      <ul class="checklist">
        <li>Brick, Block &amp; Stone replacement</li><li>Tuck pointing</li><li>Through wall flashing</li>
        <li>Coating (Sealer, Elastomeric, Silicone</li><li class="continued">and Architectural coatings)</li>
      </ul>
      <h3 class="group-title">Sealant Replacement</h3>
      <ul class="checklist">
        <li>Window wall and glazing system sealants</li><li>Precast sealants</li><li>Masonry sealants</li><li>Balcony perimeter joints</li>
      </ul>
      <h3 class="group-title">Waterproofing</h3>
      <ul class="checklist">
        <li>Balconies &amp; Terraces thin system</li><li>Garbage &amp; Mechanical rooms</li>
      </ul>
      <h2 class="section-title">Parking<br>Garage Structures:</h2>
      <div class="title-rule"></div>
      <h3 class="group-title">Concrete repairs</h3>
      <ul class="checklist">
        <li>Partial slab replacement</li><li>Top/under side repairs</li><li>Hydro demolition</li>
        <li>Columns, Beams and Shear Walls</li><li>Catch basins &amp; trench drains</li><li>Staircases</li>
      </ul>
    </section>

    <section class="panel panel--text panel--services-extra">
      <h3 class="group-title">Waterproofing</h3>
      <ul class="checklist">
        <li>Vehicular thin system (drive aisles,</li><li class="continued">parking bays, ramps, etc.)</li>
        <li>Hot applied waterproofing (Ramps</li><li class="continued">and Roof decks)</li>
        <li>Expansion joints repairs/replacement</li><li>Mastic waterproofing system</li>
        <li>Foundation wall crack injections</li><li>Crystalline waterproofing</li>
      </ul>
      <h3 class="group-title">Ramp Remediation</h3>
      <ul class="checklist">
        <li>Electric heating cables</li><li>Asphalt, interlocking, Mastic and</li><li class="continued">Concrete</li>
      </ul>
      <h2 class="section-title">Miscellaneous</h2>
      <div class="title-rule"></div>
      <ul class="checklist">
        <li>Railings remediation and replacement</li><li>Outside garbage pad enclosures</li>
        <li>Retaining walls repair/replacement</li><li>Weeping tile systems</li>
        <li>Safety bollards &amp; precast curbs installation</li><li>Side walks, curbs, interlocking, asphalt</li>
        <li class="continued">and concrete pads</li><li>Balconies and Parking garages painting</li>
        <li>Area drains replacements</li><li>Etc.</li>
      </ul>
      <svg class="footer-art" viewBox="0 0 370 250" preserveAspectRatio="none" aria-hidden="true">
        <path d="M0 120 Q200 70 370 40 V250 H0 Z" fill="#ffffff"/>
        <path d="M0 200 Q220 160 370 110 V250 H0 Z" fill="#1b1b1b"/>
      </svg>
      <div class="hat-photo" role="img" aria-label="Photo of a yellow construction hard hat"></div>
    </section>
  </main>
</body>
</html>
```